Wine Label - Design required by La Brisuela

2 Independent chilean winemakers here!
La Brisuela (means door slam or slam), that is the brand for our wines (2 wines at the moment), low scale production.
We would like to have front label for our wine out of the mainstream typical french classic style. Some words to describe it: youthful yet vintage/ Tobiah Vance/ pellman/ comic/ old western. Something i would wear on a t-shirt.
The text that is has to be on the label:
- La Brisuela (the brand)
-Field Blend (the type of one of the wines we have)
- 2018
- Wine of Chile.
It goes on sloping shoulder bottle, Burgundy model.
It is meant to cover a space of 3 1/4 h x 4 1/2 w inches . (or 8,5 cm height x 11cm width).
We like colours so...be creative!
I have attached the "La Brisuela" logo. We can changed it of course.
Thanks !

Target Market(s)

young drinkers (legally allowed to drink!)

Font styles to use
Other font styles liked:
• stencil

Colors

Designer to choose colors to be used in the design.

Requirements
Should not have
• Obvious wine things like glasses of wine, vines, grapes etc.

```html
<!DOCTYPE html>
<html lang="en">
<head>
<meta charset="utf-8">
<title>La Brisuela — Field Blend Label</title>
<link rel="stylesheet" href="https://fonts.googleapis.com/css2?family=Abril+Fatface&family=Arimo:wght@400;700&display=swap">
<style>
  :root {
    --backdrop: #1c1c1c;
    --paper: #e8e0d0;
    --ink: #1c1a1a;
    --wine-red: #982b39;
    --ornament-tone: #cfc5b2;
    --accent-tint: #c98f96;
  }
  html, body {
    margin: 0;
    padding: 0;
    width: 1200px;
    height: 792px;
    overflow: hidden;
    background: var(--backdrop);
  }
  .stage {
    position: relative;
    width: 1200px;
    height: 792px;
  }
  .wine-label {
    position: absolute;
    left: 146px;
    top: 46px;
    width: 907px;
    height: 700px;
    display: block;
  }
  .label-paper { fill: var(--paper); }
  .frame-line { fill: none; stroke: var(--ink); stroke-width: 1.6; }
  .frame-line--thin { stroke-width: 1; }
  .panel-box { fill: var(--paper); stroke: var(--ink); stroke-width: 1.6; }
  .stripe { stroke: var(--ink); stroke-width: 1.4; }
  .corner-ornament { fill: var(--ornament-tone); }
  .star-band { fill: var(--ink); opacity: 0.75; }
  .diamond-band { fill: var(--accent-tint); }
  .brand-name {
    font-family: "Abril Fatface", serif;
    font-size: 28px;
    letter-spacing: 1.5px;
    fill: var(--ink);
  }
  .wine-type {
    font-family: "Abril Fatface", serif;
    font-size: 82px;
  }
  .wine-type--field { fill: var(--ink); }
  .wine-type--blend { fill: var(--wine-red); }
  .detail-text {
    font-family: "Arimo", Arial, sans-serif;
    fill: var(--ink);
  }
  .detail-text--large { font-size: 17px; }
  .detail-text--small { font-size: 12px; font-weight: 700; }
</style>
</head>
<body>
<main class="stage">
  <svg class="wine-label" viewBox="0 0 656 506" xmlns="http://www.w3.org/2000/svg" aria-label="La Brisuela Field Blend wine label">
    <rect class="label-paper" x="0" y="0" width="656" height="506"/>

    <!-- striped bands top and bottom -->
    <g class="stripe-bands">
      <line class="stripe" x1="225" y1="4" x2="431" y2="4"/>
      <line class="stripe" x1="220" y1="9" x2="436" y2="9"/>
      <line class="stripe" x1="215" y1="14" x2="441" y2="14"/>
      <line class="stripe" x1="210" y1="19" x2="446" y2="19"/>
      <line class="stripe" x1="205" y1="24" x2="451" y2="24"/>
      <line class="stripe" x1="200" y1="29" x2="456" y2="29"/>
      <line class="stripe" x1="195" y1="34" x2="461" y2="34"/>
      <line class="stripe" x1="190" y1="39" x2="466" y2="39"/>
      <line class="stripe" x1="185" y1="44" x2="471" y2="44"/>
      <line class="stripe" x1="225" y1="502" x2="431" y2="502"/>
      <line class="stripe" x1="220" y1="497" x2="436" y2="497"/>
      <line class="stripe" x1="215" y1="492" x2="441" y2="492"/>
      <line class="stripe" x1="210" y1="487" x2="446" y2="487"/>
      <line class="stripe" x1="205" y1="482" x2="451" y2="482"/>
      <line class="stripe" x1="200" y1="477" x2="456" y2="477"/>
      <line class="stripe" x1="195" y1="472" x2="461" y2="472"/>
      <line class="stripe" x1="190" y1="467" x2="466" y2="467"/>
      <line class="stripe" x1="185" y1="462" x2="471" y2="462"/>
    </g>

    <!-- octagon diagonals -->
    <path class="frame-line" d="M229 0 L0 229 M427 0 L656 229 M229 506 L0 277 M427 506 L656 277"/>
    <path class="frame-line" d="M180 50 L0 230 M476 50 L656 230 M180 456 L0 276 M476 456 L656 276"/>

    <!-- outer frames -->
    <rect class="frame-line" x="37" y="50" width="582" height="406"/>
    <path class="frame-line frame-line--thin" d="M52 65 L604 65 M52 65 L52 441 L150 441 M604 65 L604 441 L480 441"/>

    <!-- corner squares -->
    <g class="corner-squares">
      <rect class="panel-box" x="21" y="34" width="31" height="31"/>
      <path class="frame-line frame-line--thin" d="M21 65 L52 34"/>
      <rect class="panel-box" x="604" y="34" width="31" height="31"/>
      <path class="frame-line frame-line--thin" d="M604 34 L635 65"/>
      <rect class="panel-box" x="21" y="441" width="31" height="31"/>
      <path class="frame-line frame-line--thin" d="M21 441 L52 472"/>
      <rect class="panel-box" x="604" y="441" width="31" height="31"/>
      <path class="frame-line frame-line--thin" d="M604 472 L635 441"/>
    </g>

    <!-- decorative areas -->
    <rect class="corner-ornament" x="58" y="74" width="36" height="56" role="img" aria-label="Filigree corner ornament"/>
    <rect class="corner-ornament" x="562" y="74" width="36" height="56" role="img" aria-label="Filigree corner ornament"/>
    <rect class="corner-ornament" x="58" y="378" width="36" height="56" role="img" aria-label="Filigree corner ornament"/>
    <rect class="corner-ornament" x="562" y="378" width="36" height="56" role="img" aria-label="Filigree corner ornament"/>

    <rect class="star-band" x="60" y="55" width="80" height="6" role="img" aria-label="Row of small stars"/>
    <rect class="star-band" x="516" y="55" width="80" height="6" role="img" aria-label="Row of small stars"/>
    <rect class="star-band" x="60" y="445" width="80" height="6" role="img" aria-label="Row of small stars"/>
    <rect class="star-band" x="516" y="445" width="80" height="6" role="img" aria-label="Row of small stars"/>
    <rect class="star-band" x="42" y="80" width="6" height="80" role="img" aria-label="Column of small stars"/>
    <rect class="star-band" x="608" y="80" width="6" height="80" role="img" aria-label="Column of small stars"/>
    <rect class="star-band" x="42" y="346" width="6" height="80" role="img" aria-label="Column of small stars"/>
    <rect class="star-band" x="608" y="346" width="6" height="80" role="img" aria-label="Column of small stars"/>

    <rect class="diamond-band" x="73" y="143" width="5" height="195" role="img" aria-label="Column of small red diamonds"/>
    <rect class="diamond-band" x="548" y="143" width="5" height="195" role="img" aria-label="Column of small red diamonds"/>

    <!-- inner panel and details table, drawn over the diagonals -->
    <rect class="panel-box" x="98" y="72" width="435" height="303"/>
    <rect class="panel-box" x="98" y="375" width="435" height="35"/>
    <rect class="panel-box" x="150" y="410" width="330" height="40"/>
    <path class="frame-line" d="M280 375 L280 410 M338 410 L338 450"/>

    <!-- text -->
    <text class="brand-name" x="316" y="120" text-anchor="middle">LA BRISUELA</text>
    <text class="wine-type wine-type--field" x="316" y="238" text-anchor="middle">Field</text>
    <text class="wine-type wine-type--blend" x="316" y="333" text-anchor="middle">Blend</text>
    <text class="detail-text detail-text--large" x="189" y="399" text-anchor="middle">2018</text>
    <text class="detail-text detail-text--large" x="406" y="399" text-anchor="middle">Wine of Chile</text>
    <text class="detail-text detail-text--small" x="244" y="435" text-anchor="middle">14% ALC. VOL</text>
    <text class="detail-text detail-text--small" x="409" y="435" text-anchor="middle">750ML</text>
  </svg>
</main>
</body>
</html>
```